We need an eye catching logo design and Business Card that portrays our business, which is the cleaning and protecting of stainless steel with an organic non chemical product. This can be separate to the company name or can incorporate it. Maybe even just the company name itself. Company Name is Gleamwell Gleamwell.
Ideal for products exposed to weather elements, ie: balustrading, enclosures, BBQs, we also supply the product so you can do it yourself (DIY).
In addition we would want to include on this card:
1. My Name (Dean Horrocks)
2. Mobile No. (TBA Later)
3. Email address (TBA Later)
4. Web address (TBA Later)
Updates

Please note that we also need suggestions on a logo, as this we do not have this either.

Please note we have update our brief to be more specific.

Thank You.

Dean

Target Market(s)

Purchasing officers and government people.

Industry/Entity Type

Steel

Colors

Designer to choose colors to be used in the design.

Requirements
Must have
• 1. Name (Dean Horrocks)
2. Mobile No. (TBA Later)
Should not have
• Should not be to busy looking

```html
<!DOCTYPE html>
<html lang="en">
<head>
<meta charset="utf-8">
<title>Gleamwell Gleamwell – Business Card</title>
<link rel="stylesheet" href="https://fonts.googleapis.com/css2?family=Mulish:wght@300;400;700&display=swap">
<style>
  :root {
    --page-bg: #e4e4e4;
    --card-front: #f4f4f2;
    --card-back: #5f5f5f;
    --logo-grey: #8a8a8a;
    --text-light: #f2f2f2;
    --text-muted: #d6d6d6;
    --icon-dark: #2e2e2e;
  }
  * { box-sizing: border-box; margin: 0; padding: 0; }
  html, body {
    width: 1200px; height: 823px; overflow: hidden;
    background: var(--page-bg);
    font-family: "Mulish", "Helvetica Neue", Arial, sans-serif;
  }
  .card-set {
    position: absolute; inset: 0;
    display: flex; align-items: center; justify-content: center; gap: 50px;
  }
  .card {
    width: 525px; height: 300px;
    position: relative;
    box-shadow: 0 6px 18px rgba(0,0,0,0.18);
  }
  .card--front { background: var(--card-front); }
  .card--back { background: var(--card-back); color: var(--text-light); }

  .brand-name {
    position: absolute; left: 50px; top: 124px;
    font-size: 44px; font-weight: 700; letter-spacing: 1px;
    color: var(--logo-grey); line-height: 1;
  }

  .holder { position: absolute; left: 48px; top: 84px; }
  .holder__name {
    font-size: 19px; font-weight: 400; letter-spacing: 0.5px;
    text-transform: uppercase; line-height: 1.1;
  }
  .holder__role { font-size: 13px; font-weight: 300; color: var(--text-muted); }

  .contact { position: absolute; left: 30px; list-style: none; font-size: 13.5px; font-weight: 300; }
  .contact--personal { top: 150px; }
  .contact--office { top: 206px; }
  .contact li { display: flex; align-items: flex-start; gap: 8px; line-height: 18px; }
  .contact .pair { display: flex; gap: 10px; }
  .contact .pair span { display: flex; align-items: center; gap: 8px; }
  .icon { width: 12px; height: 12px; fill: var(--icon-dark); flex: none; margin-top: 3px; }
  .indent { padding-left: 20px; }
</style>
</head>
<body>
<main class="card-set">
  <section class="card card--front" aria-label="Card front">
    <p class="brand-name">GLEAMWELL</p>
  </section>

  <section class="card card--back" aria-label="Card back">
    <div class="holder">
      <h1 class="holder__name">Dean Horrocks</h1>
      <p class="holder__role">Designation</p>
    </div>

    <ul class="contact contact--personal">
      <li>
        <svg class="icon" viewBox="0 0 12 12"><rect x="3" y="0" width="6" height="12" rx="1"/><rect x="4" y="1.5" width="4" height="7.5" fill="#5f5f5f"/></svg>
        +012 345 6789
      </li>
      <li>
        <svg class="icon" viewBox="0 0 12 12"><rect x="0" y="2" width="12" height="8" rx="1"/><rect x="2" y="4" width="8" height="1" fill="#5f5f5f"/><rect x="2" y="6.5" width="8" height="1" fill="#5f5f5f"/></svg>
        d.horrocks@gleamwellgleamwell.com
      </li>
    </ul>

    <ul class="contact contact--office">
      <li>
        <svg class="icon" viewBox="0 0 12 12"><path d="M6 0a4 4 0 0 0-4 4c0 3 4 8 4 8s4-5 4-8a4 4 0 0 0-4-4z"/><circle cx="6" cy="4" r="1.5" fill="#5f5f5f"/></svg>
        01 Avenue, Suite No. 123,
      </li>
      <li class="indent">Your City, Country</li>
      <li>
        <div class="pair">
          <span>
            <svg class="icon" viewBox="0 0 12 12"><circle cx="6" cy="6" r="6"/><path d="M4 3l1.5 1.5-1 1c.5 1 1 1.5 2 2l1-1L9 8l-1 1.2C5.5 9 3 6.5 3 4z" fill="#5f5f5f"/></svg>
            +012 345 6789
          </span>
          <span>
            <svg class="icon" viewBox="0 0 12 12"><rect x="3" y="0" width="6" height="4"/><rect x="0" y="4" width="12" height="6" rx="1"/><rect x="3" y="8" width="6" height="4"/></svg>
            +012 345 6780
          </span>
        </div>
      </li>
      <li>
        <svg class="icon" viewBox="0 0 12 12"><circle cx="6" cy="6" r="6"/><path d="M0 6h12M6 0c-3 3-3 9 0 12M6 0c3 3 3 9 0 12" stroke="#5f5f5f" stroke-width="0.8" fill="none"/></svg>
        www.GleamwellGleamwell.com
      </li>
    </ul>
  </section>
</main>
</body>
</html>
```